Health and Wellness Company Business Card

I need a business card design that is clean and uses modern minimalist style. The design should incorporate our logo (see attached). I would also like to use embossing on the cards so that they also have a great feel. I am open to the card using one or more colors, and these do not have to correspond to the colors in the concept paper. The card can either be one-sided or use both sides of the card.The logo uses the Avenir font.

I will need the file designed in Adobe CS and compatible with CS5.5 (Illustrator preferable) and I'll need the working file (for example: .ai) once the project is complete so that I can change the names/contact info/etc for each variation of the card.

This needs to be a memorable card for the recipient. They should think: "This is a great business card" either because of its simplicity or embossing effects or use of color.

Target Market(s)

The audience for our company has two main groups: people who pay for healthcare (insurers, companies, researcher companies) and people with chronic health conditions who are the consumers of our services and resources.

Industry/Entity Type

Business

Requirements
Must have
• Essential components of the card include: Company logo, contact Name (Mark Tolley), phone number (5808127346), email address (mtolley@brenquora.com), slogan/tagline that consists of ~30-40 characters (Use Lorem Ipsum)
Nice to have
• These fall just slightly short of "must have" to allow for design flexibility: Embossing or spot varnish effects and a splash of color
Should not have
• Designs with these components will not be successful: flashy or showy designs that are not professional in appearance, and lots of different colors

```html
<!DOCTYPE html>
<html lang="en">
<head>
<meta charset="utf-8">
<title>Brenquora Business Card</title>
<link rel="stylesheet" href="https://fonts.googleapis.com/css2?family=Nunito+Sans:wght@300;600&display=swap">
<style>
  :root {
    --backdrop: #ebe8e3;
    --card-deep: #4660aa;
    --card-light: #6479b3;
    --mark-tint: #b9c5ea;
    --tagline-tint: #aab8e3;
    --edge-shadow: rgba(30, 40, 70, 0.28);
  }
  html, body {
    margin: 0;
    width: 1200px;
    height: 900px;
    overflow: hidden;
    background: var(--backdrop);
  }
  .canvas {
    position: relative;
    width: 1200px;
    height: 900px;
  }
  .business-card {
    position: absolute;
    left: 100px;
    top: 185px;
    width: 1000px;
    height: 530px;
    border-radius: 4px;
    overflow: hidden;
    background: linear-gradient(160deg, var(--card-light) 0%, var(--card-deep) 55%, var(--card-deep) 100%);
    box-shadow: 0 14px 34px var(--edge-shadow);
    font-family: "Nunito Sans", "Avenir", sans-serif;
  }
  .brand {
    position: absolute;
    left: 90px;
    top: 200px;
    display: flex;
    align-items: center;
    gap: 30px;
  }
  .brand-name {
    margin: 0;
    font-size: 66px;
    font-weight: 300;
    letter-spacing: 0.4em;
    color: var(--mark-tint);
    line-height: 1;
    text-transform: uppercase;
    white-space: nowrap;
  }
  .brand-square {
    width: 56px;
    height: 56px;
    border-radius: 8px;
    background: var(--mark-tint);
    flex: none;
  }
  .tagline {
    position: absolute;
    left: 44px;
    right: 44px;
    bottom: 28px;
    margin: 0;
    font-size: 22px;
    font-weight: 300;
    letter-spacing: 0.01em;
    color: var(--tagline-tint);
    white-space: nowrap;
  }
</style>
</head>
<body>
  <main class="canvas">
    <section class="business-card" aria-label="Brenquora business card">
      <div class="brand">
        <h1 class="brand-name">Brenquora</h1>
        <span class="brand-square" aria-hidden="true"></span>
      </div>
      <p class="tagline">Lorem Ipsum is simply dummy text of the printing and typesetting industry.</p>
    </section>
  </main>
</body>
</html>
```